Motivational Poster Design Project

I would like to create a poster with some of my favorite quotes to hang in my office. I did a similar project in 2012 and I've uploaded the top 2 designs so you can get a better idea of what I'm looking for. I will provide feedback on your design within 24 hours of receiving it.

The poster must contain the following quotes:

"You’re only given a little spark of madness. You mustn’t lose it.”
- Dorian Falkes

“The most contrarian thing of all is not to oppose the crowd but to think for yourself.”
- Miles Crand

"I constantly see people rise in life who are not the smartest, sometimes not even the most diligent, but they are learning machines. They go to bed every night a little wiser than they were when they got up and boy does that help, particularly when you have a long run ahead of you."
- Harvey Belcott

“In theory, there’s no difference between theory and practice. But, in practice, there is.”
- Kees R. T. Ter Hoogwater

"At the end of the day, a reactionary life is a normal life. One thing is consistent in every remarkable person: they decide to do something remarkable. Don’t let the world choose who you become."
- Darvesh Kulani

“It usually takes 3-4 months to try enough that you can do a proper 80/20 analysis, then two months to design systems to scale what *is* working.”
-Ned Gowlan

“Authority is 20 percent given, 80 percent taken.”
- Harold Finchamp

“Your actions are consistent with the way the world occurs to you.”
- Gustav Lemmke
Updates

Project Deadline Extended
Reason: I am going to be travelling with no access to internet until January 5th, 2015. I am extending the project deadline until 12/31/14 and I'll make a final decision during the 1st week of January.

Target Market(s)

Personal Project

Industry/Entity Type

Learning

Requirements
Must have
• The poster will be 24" high x 36" long and printed on canvas, so the image you create needs to have a resolution of at least 2700 x 3900.
Nice to have
• I don't have an exact vision for how the poster should look, so I am totally open to you using your creativity to develop, arrange and present the content as you'd like.
• That said, I would like an image (photo or posterized image) of the person being quoted along with each quote. I do not have specific images that I would like you to use, so you will need to find the images on your own. The images don't need to be perfect... I am more interested in the poster relating the essence of the quotes and the people being quoted than I am in perfect photographic images of the people being quoted.

```html
<!DOCTYPE html>
<html lang="en">
<head>
<meta charset="utf-8">
<title>Quote Poster – Background Variants</title>
<link rel="stylesheet" href="https://fonts.googleapis.com/css2?family=Montserrat:wght@400;800&family=Arvo:wght@400;700&family=Amatic+SC:wght@700&family=Signika:wght@600&family=Architects+Daughter&family=Dancing+Script:wght@500&family=Parisienne&family=Handlee&family=Nothing+You+Could+Do&display=swap">
<style>
  :root {
    --page: #ffffff;
    --label: #111111;
    --frame: #7f9294;
    --frame-edge: #a9b8b8;
    --board-grey: #2b2b3d;
    --board-grey-glow: #3b3a52;
    --board-black: #1b2125;
    --board-black-glow: #283034;
    --chalk: #d9dcdc;
    --chalk-dim: #b9bfc0;
    --q-madness: #d6d96a;
    --q-contrarian: #e07cbc;
    --q-learning: #a9e4da;
    --q-theory: #f1a94f;
    --q-remarkable: #b9e066;
    --q-analysis: #aaa4f2;
    --q-authority: #cfd2d2;
    --q-actions: #d6a350;
    --band-grey: rgba(150, 146, 170, 0.35);
    --band-black: rgba(130, 140, 145, 0.28);
    --portrait-light: #9a9a9a;
    --portrait-dark: #2e2e2e;
  }
  * { box-sizing: border-box; margin: 0; padding: 0; }
  html, body { width: 1200px; height: 1000px; overflow: hidden; background: var(--page); }
  .canvas { position: relative; width: 1200px; height: 1000px; }

  .version-label {
    position: absolute; top: 38px; width: 560px; text-align: center;
    font-family: "Montserrat", sans-serif; color: var(--label);
  }
  .version-label h1 { font-size: 31px; font-weight: 800; line-height: 36px; }
  .version-label p { font-size: 20px; font-weight: 400; line-height: 26px; }
  .version-label--left { left: 25px; }
  .version-label--right { left: 608px; }

  .poster {
    position: absolute; top: 120px; width: 547px; height: 822px;
    background: var(--frame); border: 2px solid var(--frame-edge); padding: 8px;
  }
  .poster--grey { left: 34px; }
  .poster--black { left: 613px; }
  .board { position: absolute; inset: 8px; border-radius: 14px; overflow: hidden; }
  .poster--grey .board { background: radial-gradient(ellipse at 50% 45%, var(--board-grey-glow), var(--board-grey) 70%); }
  .poster--black .board { background: radial-gradient(ellipse at 50% 45%, var(--board-black-glow), var(--board-black) 70%); }

  .content { position: absolute; left: -8px; top: -8px; width: 545px; height: 822px; }
  .content > * { position: absolute; }

  .rule-band { height: 10px; border-top: 1px solid var(--chalk-dim); border-bottom: 1px solid var(--chalk-dim); opacity: .7; }

  .portrait { border-radius: 40%; background: radial-gradient(ellipse at 50% 40%, var(--portrait-light), var(--portrait-dark) 75%); }

  .signature { font-family: "Parisienne", cursive; font-size: 15px; line-height: 18px; color: var(--chalk); white-space: nowrap; }

  .quote { white-space: nowrap; }
  .quote--madness { font-family: "Arvo", serif; color: var(--q-madness); font-size: 13px; line-height: 17px; text-align: center; }
  .quote--madness strong { font-size: 16px; font-weight: 700; }
  .quote--contrarian { font-family: "Amatic SC", sans-serif; font-weight: 700; color: var(--q-contrarian); font-size: 17px; line-height: 19px; text-align: center; letter-spacing: .5px; }
  .learning-band { border-radius: 3px; }
  .poster--grey .learning-band { background: var(--band-grey); }
  .poster--black .learning-band { background: var(--band-black); }
  .quote--learning { font-family: "Handlee", cursive; color: var(--q-learning); font-size: 10.5px; line-height: 15px; }
  .quote--theory { font-family: "Signika", sans-serif; font-weight: 600; color: var(--q-theory); font-size: 14.5px; line-height: 17px; text-align: center; }
  .remarkable-box { border: 1px solid var(--chalk-dim); }
  .quote--remarkable { font-family: "Architects Daughter", cursive; color: var(--q-remarkable); font-size: 10.5px; line-height: 14px; }
  .box-rule { height: 4px; border-top: 1px solid var(--chalk-dim); border-bottom: 1px solid var(--chalk-dim); opacity: .6; }
  .quote--analysis { font-family: "Dancing Script", cursive; font-weight: 500; color: var(--q-analysis); font-size: 16.5px; line-height: 22px; text-align: right; }
  .divider-dots { font-family: "Arvo", serif; color: var(--chalk-dim); font-size: 10px; letter-spacing: 4px; }
  .quote--authority { font-family: "Arvo", serif; font-weight: 700; color: var(--q-authority); text-align: center; }
  .quote--authority .lead { display: block; font-size: 22px; line-height: 24px; letter-spacing: 1.5px; }
  .quote--authority .rest { display: block; font-size: 13px; line-height: 16px; letter-spacing: .5px; }
  .quote--actions { font-family: "Nothing You Could Do", cursive; color: var(--q-actions); font-size: 14px; line-height: 19px; text-align: center; }
</style>
</head>
<body>
<main class="canvas">

  <header class="version-label version-label--left">
    <h1>Original</h1>
    <p>(”Grey” Background)</p>
  </header>
  <header class="version-label version-label--right">
    <h1>Modified</h1>
    <p>(”Black” Background)</p>
  </header>

  <section class="poster poster--grey">
    <div class="board">
      <div class="content">
        <div class="rule-band" style="left:140px;top:32px;width:265px"></div>

        <div class="portrait" role="img" aria-label="Portrait of Dorian Falkes" style="left:355px;top:48px;width:50px;height:58px"></div>
        <p class="quote quote--madness" style="left:125px;top:58px;width:230px">"You're only given a<br>little spark of madness.<br><strong>You mustn't lose it."</strong></p>
        <p class="signature" style="left:232px;top:112px">Dorian Falkes</p>

        <div class="portrait" role="img" aria-label="Portrait of Miles Crand" style="left:62px;top:135px;width:48px;height:60px"></div>
        <p class="quote quote--contrarian" style="left:165px;top:150px;width:320px">"The most contrarian thing of all is not to<br>oppose the crowd but to think for yourself."</p>
        <p class="signature" style="left:362px;top:189px">Miles Crand</p>

        <div class="learning-band" style="left:35px;top:213px;width:440px;height:104px"></div>
        <p class="quote quote--learning" style="left:50px;top:224px">"I constantly see people rise in life who are not the smartest,<br>sometimes not even the most diligent, but they are learning machines.<br>They go to bed every night a little wiser than they were when they got up<br>and boy does that help, particularly when you have a long run ahead of you."</p>
        <div class="portrait" role="img" aria-label="Portrait of Harvey Belcott" style="left:423px;top:220px;width:50px;height:80px"></div>
        <p class="signature" style="left:72px;top:291px">Harvey Belcott</p>

        <div class="portrait" role="img" aria-label="Portrait of Kees R. T. Ter Hoogwater" style="left:125px;top:324px;width:45px;height:80px"></div>
        <p class="quote quote--theory" style="left:225px;top:328px;width:220px">"In theory, there's no difference<br>between theory and practice.<br>But, in practice, there is."</p>
        <p class="signature" style="left:300px;top:382px">Kees R. T. Ter Hoogwater</p>

        <div class="remarkable-box" style="left:45px;top:410px;width:420px;height:90px"></div>
        <p class="quote quote--remarkable" style="left:70px;top:418px">"At the end of the day, a reactionary life is a normal life.<br>One thing is consistent in every remarkable person:<br>they decide to do something remarkable.<br>Don't let the world choose who you become."</p>
        <div class="portrait" role="img" aria-label="Portrait of Darvesh Kulani" style="left:418px;top:422px;width:45px;height:55px"></div>
        <p class="signature" style="left:82px;top:477px">Darvesh Kulani</p>
        <div class="box-rule" style="left:45px;top:505px;width:420px"></div>

        <div class="portrait" role="img" aria-label="Portrait of Ned Gowlan" style="left:47px;top:514px;width:53px;height:63px"></div>
        <p class="quote quote--analysis" style="left:110px;top:514px;width:360px">"It usually takes 3-4 months to try enough that you can<br>do a proper 80/20 analysis, then two months to<br>design systems to scale what *is* working."</p>
        <p class="signature" style="left:380px;top:582px">Ned Gowlan</p>

        <p class="divider-dots" style="left:262px;top:602px">...</p>
        <svg style="left:55px;top:618px" width="415" height="62" viewBox="0 0 415 62" aria-hidden="true">
          <g fill="none" stroke="var(--chalk-dim)" stroke-width="1.2">
            <path d="M40 4 H375"/>
            <path d="M18 4 Q4 4 6 18 Q8 31 0 31 Q8 31 6 44 Q4 58 18 58"/>
            <path d="M397 4 Q411 4 409 18 Q407 31 415 31 Q407 31 409 44 Q411 58 397 58"/>
          </g>
        </svg>
        <p class="quote quote--authority" style="left:90px;top:630px;width:250px"><span class="lead">"AUTHORITY IS</span><span class="rest">20% GIVEN, 80% TAKEN."</span></p>
        <div class="portrait" role="img" aria-label="Portrait of Harold Finchamp" style="left:385px;top:628px;width:45px;height:57px"></div>
        <p class="signature" style="left:210px;top:669px">Harold Finchamp</p>

        <div class="portrait" role="img" aria-label="Portrait of Gustav Lemmke" style="left:97px;top:697px;width:43px;height:50px"></div>
        <p class="quote quote--actions" style="left:160px;top:706px;width:290px">"Your actions are consistent with<br>the way the world occurs to you."</p>
        <p class="signature" style="left:258px;top:746px">Gustav Lemmke</p>

        <div class="rule-band" style="left:140px;top:785px;width:265px"></div>
      </div>
    </div>
  </section>

  <section class="poster poster--black">
    <div class="board">
      <div class="content">
        <div class="rule-band" style="left:140px;top:32px;width:265px"></div>

        <div class="portrait" role="img" aria-label="Portrait of Dorian Falkes" style="left:355px;top:48px;width:50px;height:58px"></div>
        <p class="quote quote--madness" style="left:125px;top:58px;width:230px">"You're only given a<br>little spark of madness.<br><strong>You mustn't lose it."</strong></p>
        <p class="signature" style="left:232px;top:112px">Dorian Falkes</p>

        <div class="portrait" role="img" aria-label="Portrait of Miles Crand" style="left:62px;top:135px;width:48px;height:60px"></div>
        <p class="quote quote--contrarian" style="left:165px;top:150px;width:320px">"The most contrarian thing of all is not to<br>oppose the crowd but to think for yourself."</p>
        <p class="signature" style="left:362px;top:189px">Miles Crand</p>

        <div class="learning-band" style="left:35px;top:213px;width:440px;height:104px"></div>
        <p class="quote quote--learning" style="left:50px;top:224px">"I constantly see people rise in life who are not the smartest,<br>sometimes not even the most diligent, but they are learning machines.<br>They go to bed every night a little wiser than they were when they got up<br>and boy does that help, particularly when you have a long run ahead of you."</p>
        <div class="portrait" role="img" aria-label="Portrait of Harvey Belcott" style="left:423px;top:220px;width:50px;height:80px"></div>
        <p class="signature" style="left:72px;top:291px">Harvey Belcott</p>

        <div class="portrait" role="img" aria-label="Portrait of Kees R. T. Ter Hoogwater" style="left:125px;top:324px;width:45px;height:80px"></div>
        <p class="quote quote--theory" style="left:225px;top:328px;width:220px">"In theory, there's no difference<br>between theory and practice.<br>But, in practice, there is."</p>
        <p class="signature" style="left:300px;top:382px">Kees R. T. Ter Hoogwater</p>

        <div class="remarkable-box" style="left:45px;top:410px;width:420px;height:90px"></div>
        <p class="quote quote--remarkable" style="left:70px;top:418px">"At the end of the day, a reactionary life is a normal life.<br>One thing is consistent in every remarkable person:<br>they decide to do something remarkable.<br>Don't let the world choose who you become."</p>
        <div class="portrait" role="img" aria-label="Portrait of Darvesh Kulani" style="left:418px;top:422px;width:45px;height:55px"></div>
        <p class="signature" style="left:82px;top:477px">Darvesh Kulani</p>
        <div class="box-rule" style="left:45px;top:505px;width:420px"></div>

        <div class="portrait" role="img" aria-label="Portrait of Ned Gowlan" style="left:47px;top:514px;width:53px;height:63px"></div>
        <p class="quote quote--analysis" style="left:110px;top:514px;width:360px">"It usually takes 3-4 months to try enough that you can<br>do a proper 80/20 analysis, then two months to<br>design systems to scale what *is* working."</p>
        <p class="signature" style="left:380px;top:582px">Ned Gowlan</p>

        <p class="divider-dots" style="left:262px;top:602px">...</p>
        <svg style="left:55px;top:618px" width="415" height="62" viewBox="0 0 415 62" aria-hidden="true">
          <g fill="none" stroke="var(--chalk-dim)" stroke-width="1.2">
            <path d="M40 4 H375"/>
            <path d="M18 4 Q4 4 6 18 Q8 31 0 31 Q8 31 6 44 Q4 58 18 58"/>
            <path d="M397 4 Q411 4 409 18 Q407 31 415 31 Q407 31 409 44 Q411 58 397 58"/>
          </g>
        </svg>
        <p class="quote quote--authority" style="left:90px;top:630px;width:250px"><span class="lead">"AUTHORITY IS</span><span class="rest">20% GIVEN, 80% TAKEN."</span></p>
        <div class="portrait" role="img" aria-label="Portrait of Harold Finchamp" style="left:385px;top:628px;width:45px;height:57px"></div>
        <p class="signature" style="left:210px;top:669px">Harold Finchamp</p>

        <div class="portrait" role="img" aria-label="Portrait of Gustav Lemmke" style="left:97px;top:697px;width:43px;height:50px"></div>
        <p class="quote quote--actions" style="left:160px;top:706px;width:290px">"Your actions are consistent with<br>the way the world occurs to you."</p>
        <p class="signature" style="left:258px;top:746px">Gustav Lemmke</p>

        <div class="rule-band" style="left:140px;top:785px;width:265px"></div>
      </div>
    </div>
  </section>

</main>
</body>
</html>
```